Tamsel Naturopathics business card design

Using the tamsel logo designed, we would like that incorporated into a business card. A colour scheme which works with the logo and lists the following business details:

Lowen Tamsel - Naturopath
Level 1, 57 Orrick Street
Harrowdale NSW
(02) 4813 7096
www.lowentamselnaturo.example

We would also like space on the back of the card for next appointment times.

Target Market(s)

Anyone looking to improve their health

Industry/Entity Type

Business

Requirements
Must have
• Tamsel Naturopathics logo, business details.
Nice to have
• Good colour schemes, attractive, eye-catching features that are easy to read.

```html
<!DOCTYPE html>
<html lang="en">
<head>
<meta charset="utf-8">
<title>Tamsel Naturopathics – Business Card</title>
<link rel="stylesheet" href="https://fonts.googleapis.com/css2?family=Cinzel:wght@400;600&display=swap">
<style>
  :root {
    --stage: #e9ebee;
    --card-white: #ffffff;
    --card-mist: #dfe6ee;
    --brand-blue: #1c6fb8;
    --sky-blue: #2196de;
    --sky-blue-light: #4fb3ee;
    --navy: #0c2a52;
    --navy-light: #17406f;
    --lime: #c9dc6c;
    --text-light: #ffffff;
    --text-soft: #e4ecf5;
  }
  * { margin: 0; padding: 0; box-sizing: border-box; }
  html, body { width: 1200px; height: 867px; overflow: hidden; }
  body {
    background: var(--stage);
    font-family: "Cinzel", serif;
    position: relative;
  }
  .card {
    position: absolute;
    width: 540px;
    height: 310px;
    border-radius: 14px;
    overflow: hidden;
    box-shadow: 0 10px 24px rgba(0,0,0,0.18);
  }
  .card-back {
    left: 45px;
    top: 280px;
    background: linear-gradient(180deg, var(--card-white) 0%, var(--card-mist) 100%);
    display: flex;
    align-items: center;
    justify-content: center;
  }
  .card-front {
    left: 615px;
    top: 280px;
    background: var(--card-white);
  }
  .brand-name {
    color: var(--brand-blue);
    font-weight: 600;
    text-align: center;
    line-height: 1.15;
    letter-spacing: 0.06em;
  }
  .card-back .brand-name { font-size: 34px; }
  .front-logo-area {
    position: absolute;
    left: 0; top: 0;
    width: 258px;
    height: 270px;
    display: flex;
    align-items: center;
    justify-content: center;
  }
  .card-front .brand-name { font-size: 23px; }
  .divider {
    position: absolute;
    left: 258px; top: 0;
    width: 4px; height: 270px;
    background: var(--lime);
  }
  .details-panel {
    position: absolute;
    left: 262px; top: 0;
    width: 278px; height: 270px;
    background: linear-gradient(135deg, var(--navy) 0%, var(--navy-light) 100%);
    padding: 56px 0 0 40px;
    color: var(--text-light);
  }
  .person-name {
    font-size: 20px;
    font-weight: 600;
    letter-spacing: 0.05em;
  }
  .person-role {
    font-size: 11px;
    color: var(--sky-blue-light);
    letter-spacing: 0.12em;
    margin-top: 1px;
  }
  .contact {
    margin-top: 44px;
    font-size: 12px;
    line-height: 1.3;
    color: var(--text-soft);
    font-style: normal;
  }
  .web-band {
    position: absolute;
    left: 0; bottom: 0;
    width: 540px; height: 40px;
    background: linear-gradient(180deg, var(--sky-blue-light) 0%, var(--sky-blue) 100%);
    color: var(--text-light);
    font-size: 15px;
    letter-spacing: 0.05em;
    display: flex;
    align-items: center;
    justify-content: center;
  }
</style>
</head>
<body>
  <section class="card card-back" aria-label="Card back">
    <p class="brand-name">Tamsel<br>Naturopathics</p>
  </section>

  <section class="card card-front" aria-label="Card front">
    <div class="front-logo-area">
      <p class="brand-name">Tamsel<br>Naturopathics</p>
    </div>
    <div class="divider"></div>
    <div class="details-panel">
      <h1 class="person-name">LOWEN TAMSEL</h1>
      <p class="person-role">NATUROPATH</p>
      <address class="contact">
        LEVEL 1<br>
        57 ORRICK STREET<br>
        HARROWDALE NSW<br>
        (02) 4813 7096
      </address>
    </div>
    <div class="web-band">WWW.LOWENTAMSELNATURO.EXAMPLE</div>
  </section>
</body>
</html>
```